Vitamin Business Needs a Label Design

Hello. We are high-quality/healthy vitamin/supplement company, and we are in need of a Label design for a vitamin bottle.
Bottle will be either white or brown color. Label size will be 74mm*220mm. Please pick one logo from the attachments(you may use new design for the logo if you'd like to). On the front, please put two icon graphics(like certified organic sticker on food products) for "Kosher Certified" and "Vegetable Capsules". I attached sample of icon for your reference. I'm attaching files for the information. I will also put some example label designs on the brief page. Please let me know if you have any question. Thank you so much for the works!

Font styles to use
Serif
Sans Serif

Requirements
Must have
• Information on the files. I may put barcode later, so if possible, please leave a space for barcode. Thank you.
Nice to have
• White or Ivory color for the label background would be nice. But you may use different color if you'd like to. For your information, I prefer logo 2 over logo 1, but you can use any logo as long as the design looks great.
Should not have
• Please do not use sample icon or use icon from online. It is because there may be copyright issues. For color, please do not use dark colors for label background color. (if it looks very good, then its okay).

```html
<!DOCTYPE html>
<html lang="en">
<head>
<meta charset="utf-8">
<title>Verdalis Multivitamin Label</title>
<link rel="stylesheet" href="https://fonts.googleapis.com/css2?family=Montserrat:wght@600;700&family=Open+Sans:ital,wght@1,700;1,800&display=swap">
<style>
  :root {
    --bg: #e6e6e6;
    --label: #ffffff;
    --ink: #1c1c1c;
    --green-deep: #1f7a25;
    --green: #2f8f2c;
    --green-mid: #5aac33;
    --green-light: #a9d468;
    --green-pale: #d6ecab;
    --gold: #c99a2e;
    --gold-light: #f0d37a;
    --navy: #24408e;
    --white: #ffffff;
  }
  * { margin: 0; padding: 0; box-sizing: border-box; }
  html, body { width: 1200px; height: 960px; overflow: hidden; background: var(--bg); }
  .label {
    position: absolute; left: 300px; top: 120px; width: 600px; height: 720px;
    background: var(--label); overflow: hidden;
    box-shadow: 0 6px 24px rgba(0,0,0,.12);
  }
  .label__waves { position: absolute; inset: 0; }
  .brand {
    position: absolute; top: 70px; left: 0; right: 0;
    display: flex; justify-content: center; align-items: center; gap: 14px;
    font-family: "Montserrat", sans-serif; font-weight: 600; font-size: 62px;
    color: var(--ink);
  }
  .brand__dot { width: 20px; height: 20px; border-radius: 50%; background: var(--green-mid); }
  .product-line {
    position: absolute; top: 180px; left: 0; right: 0; text-align: center;
    font-family: "Montserrat", sans-serif; font-weight: 700; color: var(--green);
  }
  .product-line__sub { font-size: 27px; letter-spacing: .2px; }
  .product-line__main { font-size: 66px; line-height: 1.05; color: var(--green-deep); }
  .benefits {
    position: absolute; left: 40px; top: 415px;
    font-family: "Open Sans", sans-serif; font-style: italic; color: var(--white);
    text-shadow: 0 1px 3px rgba(0,0,0,.35);
  }
  .benefits__intro { font-size: 24px; font-weight: 700; margin-bottom: 2px; }
  .benefits__list { list-style: none; font-size: 36px; font-weight: 800; line-height: 1.2; }
  .benefits__list li::before { content: "•"; font-size: 24px; margin-right: 8px; vertical-align: middle; }
  .badges { position: absolute; left: 430px; top: 390px; display: flex; flex-direction: column; gap: 22px; }
  .badge { width: 104px; height: 104px; border-radius: 50%; border: 5px solid var(--gold-light); }
  .badge--kosher { background: radial-gradient(circle, var(--gold-light) 0%, var(--gold) 70%); }
  .badge--veg { background: linear-gradient(180deg, var(--navy) 0 45%, var(--gold) 45% 100%); }
  .pack-info {
    position: absolute; left: 0; right: 0; top: 640px; text-align: center;
    font-family: "Open Sans", sans-serif; font-style: italic; font-weight: 700;
    font-size: 26px; line-height: 1.3; color: var(--white);
    text-shadow: 0 1px 3px rgba(0,0,0,.35);
  }
</style>
</head>
<body>
  <main class="label">
    <svg class="label__waves" viewBox="0 0 600 720" preserveAspectRatio="none" aria-hidden="true">
      <path d="M0 290 C200 300 400 380 600 470 L600 720 L0 720Z" fill="var(--green-light)"/>
      <path d="M0 318 C200 330 400 410 600 505 L600 720 L0 720Z" fill="var(--green-mid)"/>
      <path d="M0 360 C200 380 390 450 600 560 L600 720 L0 720Z" fill="var(--green)"/>
      <path d="M0 470 C160 470 330 560 600 620" fill="none" stroke="var(--green-pale)" stroke-width="26" opacity=".7"/>
      <path d="M0 520 C180 530 360 610 600 680" fill="none" stroke="var(--green-light)" stroke-width="34" opacity=".65"/>
      <path d="M0 300 C200 312 400 392 600 485" fill="none" stroke="var(--green-pale)" stroke-width="4"/>
      <path d="M0 600 C200 620 380 690 520 720 L0 720Z" fill="var(--green-deep)" opacity=".5"/>
    </svg>

    <div class="brand"><span class="brand__name">Verdalis</span><span class="brand__dot"></span></div>

    <div class="product-line">
      <p class="product-line__sub">Multivitamin/Multimineral</p>
      <p class="product-line__main">Supplement</p>
    </div>

    <div class="benefits">
      <p class="benefits__intro">Essential support for:</p>
      <ul class="benefits__list">
        <li>Overall Health</li>
        <li>Immune System</li>
        <li>Energy</li>
        <li>Metabolism</li>
      </ul>
    </div>

    <div class="badges">
      <div class="badge badge--kosher" role="img" aria-label="Kosher certified badge"></div>
      <div class="badge badge--veg" role="img" aria-label="Vegetarian capsules badge"></div>
    </div>

    <div class="pack-info">
      <p>Dietary Supplement</p>
      <p>180 Capsules</p>
    </div>
  </main>
</body>
</html>
```